Simple Business Cards for Self-employed Coach

Simple business card with a design that includes the QLT logo.
Using either only the logo color or additional colors that match the logo.

Meridian Guides reach deeply into the past, gathering wisdom from East and West, while still staying current with the frontiers of new discovery in cognitive science, genetics, and other disciplines. see https://www.brightharborpath.example/what-is-integral-coaching/

Target Market(s)

Coaching Clients in Tokyo /Asia; in business organizations, but also outside

Industry/Entity Type

Life Coaching

Contact Information for Business Card

Lukas Brenning
Certified Meridian Guide

3-2-48 Kamiyoshi
Nakarino 164-0392
Tokyo, Japan

Phone: +81 70 4817 5062
E-Mail: lukas.brenning@mailora.example

Font styles to use
Sans Serif

Colors
00a990

Requirements
Must have
• include uploaded logo
• color fitting with QLT logo color
Nice to have
• simple, elegant design
Should not have
• clutter

```html
<!DOCTYPE html>
<html lang="en">
<head>
<meta charset="utf-8">
<title>QLT Meridian Guide — Business Card</title>
<link rel="stylesheet" href="https://fonts.googleapis.com/css2?family=Didact+Gothic&family=Open+Sans:wght@400&display=swap">
<style>
  :root {
    --page: #ffffff;
    --ink: #231f20;
    --card-dark: #000000;
    --card-light: #ffffff;
    --on-dark: #ffffff;
    --shadow: rgba(0, 0, 0, 0.35);
  }
  html, body {
    margin: 0;
    padding: 0;
    width: 1200px;
    height: 995px;
    overflow: hidden;
    background: var(--page);
  }
  .canvas {
    position: relative;
    width: 1200px;
    height: 995px;
  }
  .card {
    position: absolute;
    left: 205px;
    width: 855px;
    height: 408px;
  }
  .card--back {
    top: 27px;
    background: var(--card-dark);
  }
  .card--front {
    top: 496px;
    background: var(--card-light);
    box-shadow: 8px 14px 26px var(--shadow);
  }
  .brand {
    position: absolute;
    font-family: "Open Sans", sans-serif;
    font-weight: 400;
    line-height: 1;
  }
  .brand__row {
    display: flex;
    align-items: center;
  }
  .brand__square {
    display: block;
    background: currentColor;
  }
  .brand__name {
    letter-spacing: 0.35em;
  }
  .brand__tag {
    display: block;
    letter-spacing: 0.04em;
  }
  .card--back .brand {
    color: var(--on-dark);
    left: 258px;
    top: 152px;
  }
  .card--back .brand__square { width: 58px; height: 58px; margin-right: 30px; }
  .card--back .brand__name { font-size: 64px; }
  .card--back .brand__tag { font-size: 32px; margin-top: 16px; }
  .card--front .brand {
    color: var(--ink);
    left: 62px;
    top: 166px;
  }
  .card--front .brand__square { width: 46px; height: 46px; margin-right: 22px; }
  .card--front .brand__name { font-size: 50px; }
  .card--front .brand__tag { font-size: 24px; margin-top: 12px; }
  .divider {
    position: absolute;
    left: 360px;
    top: 66px;
    width: 2px;
    height: 292px;
    background: var(--ink);
  }
  .contact {
    position: absolute;
    left: 400px;
    top: 76px;
    color: var(--ink);
    font-family: "Didact Gothic", sans-serif;
    font-variant: small-caps;
    text-transform: none;
    margin: 0;
  }
  .contact__name {
    margin: 0;
    font-size: 38px;
    font-weight: 400;
    letter-spacing: 0.1em;
    line-height: 1;
  }
  .contact__title {
    margin: 14px 0 0;
    font-size: 21px;
    letter-spacing: 0.13em;
  }
  .contact__address,
  .contact__lines {
    margin: 28px 0 0 2px;
    font-style: normal;
    font-size: 21px;
    letter-spacing: 0.13em;
    line-height: 28px;
  }
  .contact__lines { margin-top: 33px; margin-left: 0; }
  .contact__lines p { margin: 0; }
</style>
</head>
<body>
<main class="canvas">
  <section class="card card--back" aria-label="Card back">
    <div class="brand">
      <div class="brand__row">
        <span class="brand__square"></span>
        <span class="brand__name">QLT</span>
      </div>
      <span class="brand__tag">MERIDIAN GUIDE</span>
    </div>
  </section>

  <section class="card card--front" aria-label="Card front">
    <div class="brand">
      <div class="brand__row">
        <span class="brand__square"></span>
        <span class="brand__name">QLT</span>
      </div>
      <span class="brand__tag">MERIDIAN GUIDE</span>
    </div>
    <div class="divider"></div>
    <div class="contact">
      <h1 class="contact__name">Lukas Brenning</h1>
      <p class="contact__title">Certified Meridian Guide</p>
      <address class="contact__address">
        3-2-48 Kamiyoshi<br>
        Nakarino 164-0392<br>
        Tokyo, Japan
      </address>
      <div class="contact__lines">
        <p>Phone: +81 70 4817 5062</p>
        <p>E-Mail: lukas.brenning@mailora.example</p>
      </div>
    </div>
  </section>
</main>
</body>
</html>
```